Powerpoint template for Presenting Java Related Training

I am launching a website in 2017 called Quill Harbor Labs that will offer training on advanced topics in Java programming. I need a Powerpoint template for use in the training courses. I have attached my logo. I am also attaching my business card design which was just completed ... I'd like to stay somewhat consistent between the different media, but without making the Powerpoint template too busy.
Updates

Project Deadline Extended Reason: Only 3 designs received and 2 days left so I am extending the deadline by 5 days. I would like to have at least 5 or 6 designs to consider before I make my decision. Added Sunday, October 30, 2016

Target Market(s)

Current and Prospective Software Developers

Industry/Entity Type

Software

Font styles to use
Serif
Sans Serif

Requirements
Must have
• Must use the provided logo and must use a color scheme that works well with the logo provided. Must be easy to read since this is for a training presentation and I don't want any distractions from the content.
Nice to have
• I would like to have alternatives for different types of content ... e.g. bullet lists vs. graphics, etc.
Should not have
• Just not too busy ... I want something that looks distinctive and nice but with minimal distractions.

```html
<!DOCTYPE html>
<html lang="en">
<head>
<meta charset="utf-8">
<title>Quill Harbor Labs – Training Presentation Template</title>
<link href="https://fonts.googleapis.com/css2?family=Roboto+Condensed:wght@400;700&family=Roboto:wght@400;700&display=swap" rel="stylesheet">
<style>
:root{
  --bg:#dcdcdd;
  --blue:#1b6cb8;
  --blue-dark:#12589c;
  --red:#e4242d;
  --grey:#6f6f70;
  --grey-light:#d9d9d9;
  --ink:#3a3a3a;
  --white:#ffffff;
}
*{box-sizing:border-box;margin:0;padding:0}
html,body{width:1200px;height:900px;overflow:hidden;background:var(--bg)}
body{font-family:'Roboto',sans-serif;color:var(--ink)}
h1,h2{font-weight:400}
.sheet{position:absolute;left:161px;top:42px;display:grid;grid-template-columns:repeat(3,281px);grid-auto-rows:158px;gap:5px}
.slide{position:relative;overflow:hidden;background:var(--white)}
.slide>*{position:absolute}
.slide.blue{background:var(--blue)}

/* shared pieces */
.title{left:10px;top:10px;font-family:'Roboto Condensed',sans-serif;font-size:8px;font-weight:400;color:var(--blue);letter-spacing:-.1px;padding-bottom:2px;border-bottom:.6px solid var(--blue)}
.title.light{color:var(--white);border-color:transparent}
.brand{display:flex;align-items:center;gap:2px;font-family:'Roboto Condensed',sans-serif;font-weight:700;color:var(--red);white-space:nowrap}
.brand i{display:block;border-radius:50%;background:var(--blue)}
.brand.mini{right:6px;top:8px;font-size:3.4px}
.brand.mini i{width:6px;height:6px}
.footer{left:0;right:0;bottom:0;height:3px;background:var(--blue)}
.footer::after{content:"";position:absolute;right:0;top:0;width:62px;height:3px;background:var(--red)}
.pageno{right:3px;bottom:4px;font-size:2.6px;color:var(--white);background:var(--red);padding:0 1px}
.photo{display:block}
.tiny{font-size:3.2px;line-height:1.35;text-align:justify}
.tiny b{color:var(--blue)}

/* welcome */
.welcome-logo{left:34px;top:26px;font-size:5px;flex-direction:column}
.welcome-logo i{width:12px;height:12px}
.welcome-band{left:0;right:0;top:52px;height:66px;background:var(--blue)}
.welcome-photo{left:0;top:58px;width:182px;height:75px;background:linear-gradient(120deg,#2b5e8e,#8fb6d8 55%,#3d78ad)}
.welcome-strip{left:0;top:133px;width:190px;height:7px;background:var(--grey-light);clip-path:polygon(0 0,100% 0,95% 100%,0 100%)}
.welcome-slash{left:180px;top:133px;width:24px;height:12px;background:var(--red);clip-path:polygon(45% 0,100% 0,55% 100%,0 100%)}
.welcome-text{right:14px;top:70px;text-align:right;color:var(--white)}
.welcome-text h1{font-family:'Roboto Condensed',sans-serif;font-size:14px;font-weight:400;line-height:1}
.welcome-text p{font-size:6px;letter-spacing:1.4px;margin-top:2px}
.welcome-text small{display:block;font-size:3.4px;margin-top:4px}

/* contents */
.toc-head{left:36px;top:50px;color:var(--white);font-family:'Roboto Condensed',sans-serif;padding-bottom:3px;border-bottom:.6px solid var(--white)}
.toc-head span{display:block;font-size:3.6px}
.toc-head strong{font-size:11px;font-weight:400}
.toc-list{left:138px;top:63px;list-style:none}
.toc-list li{display:flex;align-items:center;height:14.4px}
.toc-list em{width:9px;height:9px;border-radius:50%;background:var(--red);border:1px solid var(--white);color:var(--white);font-size:4px;font-style:normal;display:flex;align-items:center;justify-content:center;position:relative;z-index:1}
.toc-list span{margin-left:-3px;width:120px;height:7px;background:var(--grey-light);font-size:3.6px;line-height:7px;padding-left:9px;color:var(--blue-dark)}

/* vision */
.vision-photo{left:0;top:0;width:100%;height:86px;background:linear-gradient(160deg,#3c82c4,#5f9ad0 50%,#2a6aa8)}
.vision-red{left:0;top:86px;width:100%;height:72px;background:var(--red)}
.icon-disc{width:26px;height:26px;border-radius:50%;background:var(--red);border:2px solid var(--white);display:flex;align-items:center;justify-content:center}
.vision-text{width:92px;top:106px;color:var(--white);font-size:4px;line-height:1.3;text-align:center}

/* about 1 */
.about-band{left:0;right:0;top:45px;height:51px;background:var(--blue)}
.about-photo{left:91px;top:45px;right:0;height:51px;background:linear-gradient(100deg,#c9d3de,#8ab7e0 45%,#3f8ad0)}
.band-text{color:var(--white);font-size:3.4px;font-weight:700;line-height:1.35}

/* team */
.team-cell{width:59px;height:42px;padding:4px;color:var(--white);font-size:3px;line-height:1.3}
.team-cell strong{display:block;font-size:4.4px;margin-bottom:1px}
.team-cell.red{background:var(--red)}
.team-cell.blue{background:var(--blue)}
.team-cell.pic{background:linear-gradient(150deg,#e9edf1,#9fb3c7)}

/* partner */
.partner-box{left:45px;top:45px;width:169px;height:93px;background:var(--white);box-shadow:0 1px 3px rgba(0,0,0,.25);display:grid;grid-template-columns:repeat(4,1fr);gap:8px 10px;padding:10px 12px}
.partner-box span{display:block;background:var(--grey-light);border-radius:1px;height:9px;align-self:center}

/* cards */
.card{width:66px;height:36px;padding:3px;font-size:2.9px;line-height:1.3}
.card strong{display:block;font-size:3.6px;font-weight:400;margin-bottom:2px}
.card.fill-blue{background:var(--blue);color:var(--white)}
.card.fill-red{background:var(--red);color:var(--white)}
.card.outline{border:1px solid var(--red);color:var(--ink)}
.card.outline strong{color:var(--red)}

/* bullets */
.bullet{left:36px;width:230px}
.bullet::before{content:"";position:absolute;left:-4px;top:1px;width:2px;height:2px;background:var(--red)}

/* image text */
.image-photo{left:140px;top:0;right:0;bottom:0;background:linear-gradient(90deg,#e6eaee,#b8c3ce 60%,#8a98a6)}
.image-stripe{left:112px;top:0;width:60px;height:158px;background:var(--red);clip-path:polygon(78% 0,100% 0,30% 100%,8% 100%)}
.image-blue{left:0;top:0;width:150px;height:158px;background:var(--blue);clip-path:polygon(0 0,100% 0,50% 100%,0 100%)}

/* section */
.section-glow{left:0;top:0;width:100%;height:100%;background:radial-gradient(circle at 50% 55%,#2f80c9,var(--blue-dark) 75%)}
.section-disc{left:126px;top:62px;width:32px;height:32px;border-radius:50%;background:var(--white);display:flex;align-items:center;justify-content:center}
.section-rule{left:104px;top:104px;width:76px;height:.6px;background:var(--white)}
.section-title{left:0;right:0;top:108px;text-align:center;color:var(--white);font-family:'Roboto Condensed',sans-serif;font-size:8px;font-weight:400}

/* thank you */
.thanks-blue{left:0;top:0;width:100%;height:108px;background:linear-gradient(120deg,var(--blue-dark),var(--blue));clip-path:polygon(0 0,100% 0,100% 55%,66% 100%,0 100%)}
.thanks-title{right:30px;top:28px;color:var(--white);font-family:'Roboto Condensed',sans-serif;font-size:7px;font-weight:400}
.contact{right:30px;color:var(--white);font-size:3.6px;display:flex;align-items:center;gap:3px}
.contact svg{width:6px;height:6px}
.thanks-logo{right:36px;top:118px;font-size:4.6px;flex-direction:column}
.thanks-logo i{width:12px;height:12px}
.thanks-line{left:0;right:0;bottom:0;height:2px;background:var(--red)}
</style>
</head>
<body>
<main class="sheet">

  <!-- 1 Welcome -->
  <section class="slide">
    <div class="brand welcome-logo"><i></i>QUILL HARBOR LABS</div>
    <div class="welcome-band"></div>
    <div class="photo welcome-photo" role="img" aria-label="Hand touching a hexagon technology interface"></div>
    <div class="welcome-strip"></div>
    <div class="welcome-slash"></div>
    <div class="welcome-text">
      <h1>WELCOME</h1>
      <p>TO OUR PRESENTATION</p>
      <small>Ashford, August 25, 2016</small>
    </div>
  </section>

  <!-- 2 Contents -->
  <section class="slide blue">
    <div class="toc-head"><span>TABLE OF</span><strong>CONTENTS</strong></div>
    <ol class="toc-list">
      <li><em>1</em><span>LOREM IPSUM DOLOR SIT MET</span></li>
      <li><em>2</em><span>LOREM IPSUM DOLOR SIT MET</span></li>
      <li><em>3</em><span>LOREM IPSUM DOLOR SIT MET</span></li>
      <li><em>4</em><span>LOREM IPSUM DOLOR SIT MET</span></li>
      <li><em>5</em><span>LOREM IPSUM DOLOR SIT MET</span></li>
      <li><em>6</em><span>LOREM IPSUM DOLOR SIT MET</span></li>
    </ol>
  </section>

  <!-- 3 Vision & Mission -->
  <section class="slide">
    <div class="photo vision-photo" role="img" aria-label="Business team at a meeting table, blue tinted"></div>
    <div class="vision-red"></div>
    <div class="title light" style="top:14px;font-size:7px">VISION &amp; MISSION</div>
    <div class="icon-disc" style="left:61px;top:69px">
      <svg width="13" height="8" viewBox="0 0 13 8" fill="none" stroke="#fff" stroke-width="1.3"><circle cx="3.5" cy="4.5" r="2.6"/><circle cx="9.5" cy="4.5" r="2.6"/><path d="M6 4.5h1"/></svg>
    </div>
    <div class="icon-disc" style="left:179px;top:69px">
      <svg width="12" height="10" viewBox="0 0 12 10" fill="none" stroke="#fff" stroke-width="1.3"><path d="M1.5 9a4.5 4.5 0 1 1 9 0"/><path d="M6 9l2.5-3.5"/></svg>
    </div>
    <p class="vision-text" style="left:28px">To provide state of the art logistical and supply chain solutions to the defined needs of our customers using the best people, processes and systems in creating efficient and effective results.</p>
    <p class="vision-text" style="left:146px">To provide state of the art logistical and supply chain solutions to the defined needs of our customers using the best people, processes and systems in creating efficient and effective results.</p>
  </section>

  <!-- 4 About us: banner -->
  <section class="slide">
    <h2 class="title">ABOUT US</h2>
    <div class="brand mini"><i></i>QUILL HARBOR LABS</div>
    <div class="about-band"></div>
    <div class="photo about-photo" role="img" aria-label="Man touching a floating screen against a sky"></div>
    <p class="band-text" style="left:17px;top:61px;width:70px">LOREM IPSUM DOLOR SIT MET CONSECTUR ADIPISCING ELIT SED DO EIUSMOD TEMPOR</p>
    <p class="tiny" style="left:90px;top:104px;width:176px">Each module starts with a short talk, moves into live coding and ends with a lab you finish on your own. We cover memory, threads, loading and tuning, with examples drawn from production systems and clear notes to keep.</p>
    <div class="footer"></div><span class="pageno">2</span>
  </section>

  <!-- 5 About us: columns -->
  <section class="slide">
    <h2 class="title">ABOUT US</h2>
    <div class="brand mini"><i></i>QUILL HARBOR LABS</div>
    <div class="photo" role="img" aria-label="Woman working at an office desk" style="left:11px;top:35px;width:60px;height:34px;background:linear-gradient(135deg,#c7ced6,#7d8c9b)"></div>
    <p class="tiny" style="left:11px;top:72px;width:60px;text-align:right;color:var(--blue)">Short caption for the photo beside this column</p>
    <p class="tiny" style="left:82px;top:38px;width:88px">Each course is built around a single topic and one working project. You read less and write more, with hands-on labs after each short lesson and reviews that point out what to fix next time.</p>
    <p class="tiny" style="left:82px;top:94px;width:88px">Sessions are small so every question gets an answer. Notes, code and slides stay with you after the course ends, ready for your next project.</p>
    <p class="tiny" style="left:180px;top:38px;width:88px">Our trainers have shipped large systems and know where code breaks under load. They share the tools and habits that keep services fast, safe and easy to change across a growing team.</p>
    <p class="tiny" style="left:180px;top:94px;width:88px">Start with the basics of the platform, then move into profiling, concurrency and design, one clear step at a time.</p>
    <div class="footer"></div><span class="pageno">3</span>
  </section>

  <!-- 6 About us: tiles -->
  <section class="slide">
    <h2 class="title">ABOUT US</h2>
    <div class="brand mini"><i></i>QUILL HARBOR LABS</div>
    <div class="photo" role="img" aria-label="Team in a meeting room" style="left:0;top:37px;width:70px;height:43px;background:linear-gradient(135deg,#c9a98c,#6e5a4a)"></div>
    <p class="band-text" style="left:70px;top:37px;width:70px;height:43px;background:var(--red);padding:18px 4px 0">LOREM IPSUM DOLOR SIT MET CONSECTUR ADIPISCING ELIT SED DO EIUSMOD</p>
    <div class="photo" role="img" aria-label="Two colleagues reviewing a document" style="left:140px;top:37px;width:70px;height:43px;background:linear-gradient(135deg,#e3e7ea,#9aa7b2)"></div>
    <p class="band-text" style="left:210px;top:37px;width:71px;height:43px;background:var(--blue);padding:18px 4px 0">LOREM IPSUM DOLOR SIT MET CONSECTUR ADIPISCING ELIT SED DO EIUSMOD</p>
    <p class="band-text" style="left:0;top:80px;width:70px;height:62px;background:var(--grey);padding:20px 4px 0">LOREM IPSUM DOLOR SIT MET CONSECTUR ADIPISCING ELIT SED DO EIUSMOD</p>
    <div class="photo" role="img" aria-label="Group working at laptops" style="left:70px;top:80px;width:70px;height:62px;background:linear-gradient(135deg,#d8c2ae,#7a6352)"></div>
    <p class="band-text" style="left:140px;top:80px;width:70px;height:62px;background:var(--grey);padding:20px 4px 0">LOREM IPSUM DOLOR SIT MET CONSECTUR ADIPISCING ELIT SED DO EIUSMOD</p>
    <div class="photo" role="img" aria-label="Audience in a training room" style="left:210px;top:80px;width:71px;height:62px;background:linear-gradient(135deg,#c8a487,#6b4e3b)"></div>
    <div class="footer"></div><span class="pageno">4</span>
  </section>

  <!-- 7 Our chart: bars -->
  <section class="slide">
    <h2 class="title">OUR CHART</h2>
    <div class="brand mini"><i></i>QUILL HARBOR LABS</div>
    <p class="tiny" style="left:25px;top:48px;width:122px"><b>Lorem ipsum dolor sit amet</b><br>Students complete four labs per module and review each answer with a trainer before moving on to the next topic in the course plan.</p>
    <p class="tiny" style="left:25px;top:82px;width:122px"><b>Lorem ipsum dolor sit amet</b><br>Results are tracked across each cohort so the course keeps improving and the hard parts get more time and better examples.</p>
    <p class="tiny" style="left:25px;top:116px;width:122px"><b>Lorem ipsum dolor sit amet</b><br>Every cohort ends with a short project review and a written summary of next steps.</p>
    <svg style="left:178px;top:38px" width="86" height="54" viewBox="0 0 86 54">
      <line x1="2" y1="0" x2="2" y2="46" stroke="#999" stroke-width=".4"/>
      <line x1="2" y1="46" x2="86" y2="46" stroke="#999" stroke-width=".4"/>
      <g>
        <rect x="6" y="20" width="4" height="26" fill="#1b6cb8"/><rect x="11" y="30" width="4" height="16" fill="#12589c"/><rect x="16" y="26" width="4" height="20" fill="#e4242d"/>
        <rect x="27" y="22" width="4" height="24" fill="#1b6cb8"/><rect x="32" y="12" width="4" height="34" fill="#999"/><rect x="37" y="28" width="4" height="18" fill="#e4242d"/>
        <rect x="48" y="16" width="4" height="30" fill="#1b6cb8"/><rect x="53" y="22" width="4" height="24" fill="#12589c"/><rect x="58" y="32" width="4" height="14" fill="#999"/>
        <rect x="69" y="24" width="4" height="22" fill="#1b6cb8"/><rect x="74" y="10" width="4" height="36" fill="#e4242d"/><rect x="79" y="20" width="4" height="26" fill="#999"/>
        <rect x="31" y="6" width="6" height="3" fill="#999"/><rect x="51" y="10" width="6" height="3" fill="#1b6cb8"/><rect x="73" y="4" width="6" height="3" fill="#e4242d"/>
      </g>
      <g font-size="2.6" fill="#666" font-family="Roboto, sans-serif"><text x="8" y="51">2009</text><text x="29" y="51">2010</text><text x="50" y="51">2011</text><text x="71" y="51">2012</text></g>
    </svg>
    <div style="left:195px;top:96px;width:70px">
      <p class="tiny" style="position:relative;padding-left:6px"><span style="position:absolute;left:0;top:1px;width:3px;height:3px;background:var(--blue)"></span>LOREM IPSUM<br>Short note on this series of results</p>
      <p class="tiny" style="position:relative;padding-left:6px;margin-top:3px"><span style="position:absolute;left:0;top:1px;width:3px;height:3px;background:var(--grey)"></span>LOREM IPSUM<br>Short note on this series of results</p>
      <p class="tiny" style="position:relative;padding-left:6px;margin-top:3px"><span style="position:absolute;left:0;top:1px;width:3px;height:3px;background:var(--red)"></span>LOREM IPSUM</p>
    </div>
    <div class="footer"></div><span class="pageno">5</span>
  </section>

  <!-- 8 Our chart: donuts -->
  <section class="slide">
    <h2 class="title">OUR CHART</h2>
    <div class="brand mini"><i></i>QUILL HARBOR LABS</div>
    <svg style="left:40px;top:52px" width="32" height="32" viewBox="0 0 32 32"><circle cx="16" cy="16" r="13" fill="none" stroke="#c9c9c9" stroke-width="3"/><circle cx="16" cy="16" r="13" fill="none" stroke="#e4242d" stroke-width="3" stroke-dasharray="66.2 81.7" transform="rotate(-90 16 16)"/><text x="16" y="18.5" text-anchor="middle" font-size="7" font-weight="700" fill="#1b6cb8" font-family="Roboto Condensed, sans-serif">81%</text></svg>
    <svg style="left:123px;top:52px" width="32" height="32" viewBox="0 0 32 32"><circle cx="16" cy="16" r="13" fill="none" stroke="#c9c9c9" stroke-width="3"/><circle cx="16" cy="16" r="13" fill="none" stroke="#1b6cb8" stroke-width="3" stroke-dasharray="58.8 81.7" transform="rotate(-90 16 16)"/><text x="16" y="18.5" text-anchor="middle" font-size="7" font-weight="700" fill="#1b6cb8" font-family="Roboto Condensed, sans-serif">72%</text></svg>
    <svg style="left:202px;top:52px" width="32" height="32" viewBox="0 0 32 32"><circle cx="16" cy="16" r="13" fill="none" stroke="#c9c9c9" stroke-width="3"/><circle cx="16" cy="16" r="13" fill="none" stroke="#e4242d" stroke-width="3" stroke-dasharray="51.5 81.7" transform="rotate(-90 16 16)"/><text x="16" y="18.5" text-anchor="middle" font-size="7" font-weight="700" fill="#1b6cb8" font-family="Roboto Condensed, sans-serif">63%</text></svg>
    <p class="tiny" style="left:28px;top:94px;width:58px;text-align:center">Share of students who finish every lab in the course and pass the final project review on the first try.</p>
    <p class="tiny" style="left:110px;top:94px;width:58px;text-align:center">Share of students who finish every lab in the course and pass the final project review on the first try.</p>
    <p class="tiny" style="left:189px;top:94px;width:58px;text-align:center">Share of students who finish every lab in the course and pass the final project review on the first try.</p>
    <div class="footer"></div><span class="pageno">6</span>
  </section>

  <!-- 9 Our team -->
  <section class="slide">
    <h2 class="title">OUR TEAM</h2>
    <div class="brand mini"><i></i>QUILL HARBOR LABS</div>
    <div class="team-cell pic photo" role="img" aria-label="Portrait of a team member" style="left:19px;top:47px"></div>
    <div class="team-cell blue" style="left:19px;top:89px"><strong>Jordan Vale</strong>Senior trainer for concurrency and memory topics</div>
    <div class="team-cell red" style="left:78px;top:47px"><strong>Jordan Vale</strong>Senior trainer for concurrency and memory topics</div>
    <div class="team-cell pic photo" role="img" aria-label="Portrait of a team member" style="left:78px;top:89px"></div>
    <div class="team-cell pic photo" role="img" aria-label="Portrait of a team member" style="left:137px;top:47px"></div>
    <div class="team-cell red" style="left:137px;top:89px"><strong>Jordan Vale</strong>Senior trainer for concurrency and memory topics</div>
    <div class="team-cell blue" style="left:196px;top:47px"><strong>Jordan Vale</strong>Senior trainer for concurrency and memory topics</div>
    <div class="team-cell pic photo" role="img" aria-label="Portrait of a team member" style="left:196px;top:89px"></div>
    <div class="footer"></div><span class="pageno">7</span>
  </section>

  <!-- 10 Our partner -->
  <section class="slide">
    <h2 class="title">OUR PARTNER</h2>
    <div class="brand mini"><i></i>QUILL HARBOR LABS</div>
    <div class="partner-box" role="list" aria-label="Partner badges">
      <span role="listitem" style="background:#e9a0a3"></span><span role="listitem"></span><span role="listitem" style="background:#9bb7d6"></span><span role="listitem" style="width:9px;justify-self:center;background:#234a7a"></span>
      <span role="listitem" style="background:#9bb7d6"></span><span role="listitem" style="background:#8a8a8a"></span><span role="listitem" style="background:#8fa07a"></span><span role="listitem" style="background:#e9a0a3"></span>
      <span role="listitem"></span><span role="listitem" style="background:#f1c39a"></span><span role="listitem" style="background:#b7c9a4"></span><span role="listitem" style="width:9px;justify-self:center;border-radius:50%;background:#f2e2a0"></span>
      <span role="listitem" style="background:#9bb7d6"></span><span role="listitem"></span><span role="listitem" style="background:#9bb7d6"></span><span role="listitem"></span>
    </div>
    <div class="footer"></div><span class="pageno">8</span>
  </section>

  <!-- 11 Title goes here -->
  <section class="slide">
    <h2 class="title">TITLE GOES HERE</h2>
    <div class="brand mini"><i></i>QUILL HARBOR LABS</div>
    <p class="tiny" style="left:30px;top:46px;width:220px;text-align:center;font-style:italic;font-weight:700">Each lesson below has one clear goal and a short lab to practise it before you move on.<br>Pick the cards that fit your course and remove the rest.</p>
    <div class="card fill-blue" style="left:32px;top:63px"><strong>Lorem ipsum dolor</strong>Short summary of one key idea for this topic in the course.</div>
    <div class="card outline" style="left:107px;top:63px"><strong>Lorem ipsum dolor</strong>Short summary of one key idea for this topic in the course.</div>
    <div class="card fill-blue" style="left:182px;top:63px"><strong>Lorem ipsum dolor</strong>Short summary of one key idea for this topic in the course.</div>
    <div class="card outline" style="left:32px;top:103px"><strong>Lorem ipsum dolor</strong>Short summary of one key idea for this topic in the course.</div>
    <div class="card fill-red" style="left:107px;top:103px"><strong>Lorem ipsum dolor</strong>Short summary of one key idea for this topic in the course.</div>
    <div class="card outline" style="left:182px;top:103px"><strong>Lorem ipsum dolor</strong>Short summary of one key idea for this topic in the course.</div>
    <div class="footer"></div><span class="pageno">9</span>
  </section>

  <!-- 12 Bullet text -->
  <section class="slide">
    <h2 class="title">BULLET TEXT</h2>
    <div class="brand mini"><i></i>QUILL HARBOR LABS</div>
    <p class="tiny bullet" style="top:48px"><b>Lorem ipsum dolor sit amet</b><br>Start each bullet with the main point, then add one line of detail that the audience can read from the back of the room without strain. Keep lists short and plain.</p>
    <p class="tiny bullet" style="top:76px"><b>Lorem ipsum dolor sit amet</b><br>Start each bullet with the main point, then add one line of detail that the audience can read from the back of the room without strain. Keep lists short and plain.</p>
    <p class="tiny bullet" style="top:104px"><b>Lorem ipsum dolor sit amet</b><br>Use a code slide for anything longer than two lines, and link back to it from here so this list stays clean and easy to follow.</p>
    <div class="footer"></div><span class="pageno">10</span>
  </section>

  <!-- 13 Image text -->
  <section class="slide">
    <div class="photo image-photo" role="img" aria-label="Businesswoman holding a tablet"></div>
    <div class="image-stripe"></div>
    <div class="image-blue"></div>
    <div class="title light" style="left:16px;top:14px;font-size:7px">IMAGE TEXT</div>
    <p class="tiny" style="left:17px;top:61px;width:94px;color:var(--white);font-size:3.4px;font-weight:700">Lorem ipsum dolor sit amet. Use this layout when a single picture carries the message and the text only needs to add a short note about what to look for and why it matters to the lesson.</p>
    <div class="brand" style="left:4px;bottom:6px;font-size:3px;color:var(--white)"><i style="width:6px;height:6px;background:var(--white)"></i>QUILL HARBOR LABS</div>
  </section>

  <!-- 14 Section title -->
  <section class="slide blue">
    <div class="section-glow"></div>
    <div class="section-disc"><span class="brand" style="font-size:3px;flex-direction:column"><i style="width:9px;height:9px"></i>QUILL HARBOR</span></div>
    <div class="section-rule"></div>
    <h2 class="section-title">SECTION TITLE</h2>
  </section>

  <!-- 15 Thank you -->
  <section class="slide">
    <div class="thanks-blue"></div>
    <h2 class="thanks-title">THANK YOU</h2>
    <p class="contact" style="top:46px">120 Lantern Row Ste 4
      <svg viewBox="0 0 6 6"><circle cx="3" cy="3" r="2.7" fill="none" stroke="#fff" stroke-width=".5"/><path d="M3 1.4a1.1 1.1 0 0 1 1.1 1.1C4.1 3.4 3 4.6 3 4.6S1.9 3.4 1.9 2.5A1.1 1.1 0 0 1 3 1.4z" fill="#fff"/></svg></p>
    <p class="contact" style="top:58px">hello@quillharbor.dev
      <svg viewBox="0 0 6 6"><circle cx="3" cy="3" r="2.7" fill="none" stroke="#fff" stroke-width=".5"/><rect x="1.6" y="2" width="2.8" height="2" fill="none" stroke="#fff" stroke-width=".4"/><path d="M1.6 2L3 3.1 4.4 2" fill="none" stroke="#fff" stroke-width=".4"/></svg></p>
    <p class="contact" style="top:70px">www.quillharbor.dev
      <svg viewBox="0 0 6 6"><circle cx="3" cy="3" r="2.7" fill="none" stroke="#fff" stroke-width=".5"/><circle cx="3" cy="3" r="1.3" fill="none" stroke="#fff" stroke-width=".4"/></svg></p>
    <div class="brand thanks-logo"><i></i>QUILL HARBOR LABS</div>
    <div class="thanks-line"></div>
  </section>

</main>
</body>
</html>
```